Seasoned logs and kindling for sale

producing firewood from beech,ash,oak and silver birch,
Kindling is produce from a variety of seasoned softwoods

Industry/Entity Type

Firewood

Contact Information for Business Card

peter Calloway 07831226904
alan Frickley 07854317620
e-mail,peterc817@mailbrook.example

```html
<!DOCTYPE html>
<html lang="en">
<head>
<meta charset="utf-8">
<title>Seasoned Logs and Kindling – Business Card</title>
<link href="https://fonts.googleapis.com/css2?family=Lato:wght@400;700&display=swap" rel="stylesheet">
<style>
  :root {
    --backdrop: #6a6a6a;
    --wood-light: #f1dcae;
    --wood-mid: #e8cd98;
    --wood-dark: #dcbb82;
    --band-red: #7b2126;
    --name-red: #7b2126;
    --ink: #1c1c1c;
    --white: #ffffff;
  }
  * { margin: 0; padding: 0; box-sizing: border-box; }
  html, body {
    width: 1200px;
    height: 900px;
    overflow: hidden;
    background: var(--backdrop);
    font-family: "Lato", sans-serif;
  }
  .canvas {
    position: relative;
    width: 1200px;
    height: 900px;
  }
  .business-card {
    position: absolute;
    left: 100px;
    top: 164px;
    width: 1000px;
    height: 572px;
    overflow: hidden;
  }
  .wood-surface {
    position: absolute;
    inset: 0;
    background:
      linear-gradient(172deg, var(--wood-light) 0%, var(--wood-mid) 35%, var(--wood-light) 55%, var(--wood-dark) 80%, var(--wood-mid) 100%);
  }
  .contact-band {
    position: absolute;
    left: 0;
    top: 26px;
    width: 100%;
    height: 80px;
    background: var(--band-red);
    display: flex;
    align-items: center;
    justify-content: flex-end;
    padding-right: 34px;
    gap: 12px;
    color: var(--white);
    font-size: 23px;
    font-weight: 400;
  }
  .mail-icon { width: 22px; height: 16px; }
  .contact-person {
    position: absolute;
    top: 242px;
  }
  .contact-person--first { left: 172px; }
  .contact-person--second { left: 612px; }
  .person-name {
    color: var(--name-red);
    font-weight: 700;
    font-size: 40px;
    line-height: 1.1;
    letter-spacing: -0.3px;
  }
  .person-phone {
    display: flex;
    align-items: center;
    gap: 10px;
    margin-top: 6px;
    color: var(--ink);
    font-size: 30px;
    font-weight: 400;
    letter-spacing: 0.3px;
  }
  .phone-icon { width: 15px; height: 24px; }
</style>
</head>
<body>
<main class="canvas">
  <section class="business-card">
    <div class="wood-surface" role="img" aria-label="Light pale wood grain texture"></div>

    <div class="contact-band">
      <svg class="mail-icon" viewBox="0 0 22 16" aria-hidden="true">
        <rect x="0" y="0" width="22" height="16" rx="1.5" fill="#ffffff"/>
        <path d="M1 1.5 L11 9 L21 1.5" fill="none" stroke="#7b2126" stroke-width="2"/>
      </svg>
      <span class="contact-email">peterc817@mailbrook.example</span>
    </div>

    <div class="contact-person contact-person--first">
      <h2 class="person-name">Peter Calloway</h2>
      <p class="person-phone">
        <svg class="phone-icon" viewBox="0 0 15 24" aria-hidden="true">
          <rect x="1" y="1" width="13" height="22" rx="2.5" fill="none" stroke="#1c1c1c" stroke-width="2"/>
          <rect x="3.5" y="4" width="8" height="13" fill="#1c1c1c"/>
          <circle cx="7.5" cy="20" r="1.2" fill="#1c1c1c"/>
        </svg>
        078-312-26904
      </p>
    </div>

    <div class="contact-person contact-person--second">
      <h2 class="person-name">Alan Frickley</h2>
      <p class="person-phone">
        <svg class="phone-icon" viewBox="0 0 15 24" aria-hidden="true">
          <rect x="1" y="1" width="13" height="22" rx="2.5" fill="none" stroke="#1c1c1c" stroke-width="2"/>
          <rect x="3.5" y="4" width="8" height="13" fill="#1c1c1c"/>
          <circle cx="7.5" cy="20" r="1.2" fill="#1c1c1c"/>
        </svg>
        078-543-17620
      </p>
    </div>
  </section>
</main>
</body>
</html>
```